Bref créative
meadowlark mobile ultrasound business cards
Meadowlark Mobile Ultrasound
Bright & Fun-filled
Doreen Pavlick, RDMS, RVT
President/Owner
Palm Grove, FL 33000
info@meadowlarkmobileultrasound.example
www.meadowlarkmobileultrasound.example

```html
<!DOCTYPE html>
<html lang="en">
<head>
<meta charset="utf-8">
<title>Meadowlark Mobile Ultrasound — Stationery</title>
<link href="https://fonts.googleapis.com/css2?family=Open+Sans:wght@400;600&display=swap" rel="stylesheet">
<style>
  :root {
    --bg: #e6e6e8;
    --paper: #ffffff;
    --ink: #3a3a3a;
    --ink-soft: #8a8a8a;
    --sun-yellow: #ffd21f;
    --sun-orange: #f7931e;
    --sun-deep: #ef5a24;
    --rule: #6b6b6b;
  }
  * { box-sizing: border-box; margin: 0; padding: 0; }
  html, body { width: 1200px; height: 869px; overflow: hidden; }
  body {
    background: var(--bg);
    font-family: "Open Sans", Arial, sans-serif;
    color: var(--ink);
    position: relative;
  }
  .piece {
    position: absolute;
    background: var(--paper);
    box-shadow: 0 4px 14px rgba(0,0,0,.18);
    overflow: hidden;
  }
  .wave { position: absolute; left: 0; bottom: 0; width: 100%; display: block; }

  /* company name: one colour, one weight, one line */
  .company-name {
    font-family: "Open Sans", Arial, sans-serif;
    font-weight: 600;
    color: var(--ink);
    white-space: nowrap;
    line-height: 1.2;
  }

  /* sheets */
  .sheet { width: 340px; height: 440px; top: 30px; }
  .sheet--fax { left: 40px; }
  .sheet--letter { left: 410px; }
  .sheet .company-name {
    position: absolute; top: 30px; left: 0; right: 0;
    text-align: center; font-size: 14px;
  }

  .fax-form { position: absolute; top: 72px; left: 30px; right: 30px; font-size: 8px; }
  .fax-title { text-align: right; font-weight: 600; font-size: 13px; letter-spacing: 1px; margin-bottom: 2px; }
  .fax-table { width: 100%; border-collapse: collapse; }
  .fax-table td { border: 1px solid var(--rule); height: 17px; padding: 0 4px; }
  .fax-table td.label { width: 18%; font-weight: 600; }
  .fax-checks { display: flex; justify-content: space-between; margin-top: 6px; }
  .fax-checks span::before {
    content: ""; display: inline-block; width: 7px; height: 7px;
    border: 1px solid var(--rule); margin-right: 3px; vertical-align: -1px;
  }

  .contact {
    position: absolute; right: 16px; color: #fff; text-align: right;
    font-size: 7px; line-height: 1.45;
  }
  .sheet .contact { bottom: 12px; }

  /* envelope */
  .envelope { left: 40px; top: 510px; width: 700px; height: 330px; }
  .envelope .company-name { position: absolute; top: 30px; left: 30px; font-size: 18px; }
  .return-address { position: absolute; top: 62px; left: 30px; font-size: 9px; color: var(--ink-soft); line-height: 1.5; }
  .envelope .contact { bottom: 16px; right: 24px; font-size: 9px; }

  /* business cards */
  .card { left: 780px; width: 380px; height: 217px; border-radius: 8px; }
  .card--front { top: 80px; }
  .card--back { top: 567px; background: radial-gradient(circle at 72% 55%, var(--sun-yellow) 0%, var(--sun-orange) 45%, var(--sun-deep) 100%); }
  .card--front .company-name { position: absolute; top: 28px; left: 24px; font-size: 19px; }
  .person { position: absolute; top: 100px; left: 24px; }
  .person-name { color: var(--sun-deep); font-weight: 600; font-size: 13px; }
  .person-title { color: var(--ink-soft); font-size: 10px; }
  .card--front .contact { bottom: 12px; right: 18px; font-size: 8px; }
</style>
</head>
<body>

<!-- Fax cover sheet -->
<section class="piece sheet sheet--fax">
  <div class="company-name">Meadowlark Mobile Ultrasound</div>
  <div class="fax-form">
    <div class="fax-title">FAX</div>
    <table class="fax-table">
      <tr><td class="label">To:</td><td></td><td class="label">From:</td><td></td></tr>
      <tr><td class="label">Fax:</td><td></td><td class="label">Pages:</td><td></td></tr>
      <tr><td class="label">Phone:</td><td></td><td class="label">Date:</td><td></td></tr>
      <tr><td class="label">Re:</td><td></td><td class="label">CC:</td><td></td></tr>
    </table>
    <div class="fax-checks">
      <span>Urgent</span><span>For Review</span><span>Please Comment</span><span>Please Reply</span>
    </div>
  </div>
  <svg class="wave" viewBox="0 0 100 30" preserveAspectRatio="none" height="90" aria-hidden="true">
    <path d="M0 16 C30 8 65 4 100 0 L100 30 L0 30Z" fill="var(--sun-yellow)"/>
    <path d="M0 19 C35 12 68 9 100 5 L100 30 L0 30Z" fill="var(--sun-orange)"/>
    <path d="M0 23 C40 18 72 15 100 12 L100 30 L0 30Z" fill="var(--sun-deep)"/>
  </svg>
  <div class="contact">Palm Grove, FL 33000 · (954) 555-0142<br>www.meadowlarkmobileultrasound.example</div>
</section>

<!-- Letterhead -->
<section class="piece sheet sheet--letter">
  <div class="company-name">Meadowlark Mobile Ultrasound</div>
  <svg class="wave" viewBox="0 0 100 30" preserveAspectRatio="none" height="90" aria-hidden="true">
    <path d="M0 16 C30 8 65 4 100 0 L100 30 L0 30Z" fill="var(--sun-yellow)"/>
    <path d="M0 19 C35 12 68 9 100 5 L100 30 L0 30Z" fill="var(--sun-orange)"/>
    <path d="M0 23 C40 18 72 15 100 12 L100 30 L0 30Z" fill="var(--sun-deep)"/>
  </svg>
  <div class="contact">Palm Grove, FL 33000 · (954) 555-0142<br>info@meadowlarkmobileultrasound.example<br>www.meadowlarkmobileultrasound.example</div>
</section>

<!-- Envelope -->
<section class="piece envelope">
  <div class="company-name">Meadowlark Mobile Ultrasound</div>
  <div class="return-address">Doreen Pavlick, RDMS, RVT<br>Palm Grove, FL 33000</div>
  <svg class="wave" viewBox="0 0 100 30" preserveAspectRatio="none" height="110" aria-hidden="true">
    <path d="M0 16 C30 8 65 4 100 0 L100 30 L0 30Z" fill="var(--sun-yellow)"/>
    <path d="M0 19 C35 12 68 9 100 5 L100 30 L0 30Z" fill="var(--sun-orange)"/>
    <path d="M0 23 C40 18 72 15 100 12 L100 30 L0 30Z" fill="var(--sun-deep)"/>
  </svg>
  <div class="contact">(954) 555-0142<br>www.meadowlarkmobileultrasound.example</div>
</section>

<!-- Business card front -->
<section class="piece card card--front">
  <div class="company-name">Meadowlark Mobile Ultrasound</div>
  <div class="person">
    <div class="person-name">Doreen Pavlick, RDMS, RVT</div>
    <div class="person-title">President/Owner</div>
  </div>
  <svg class="wave" viewBox="0 0 100 30" preserveAspectRatio="none" height="80" aria-hidden="true">
    <path d="M0 24 C35 16 65 6 100 0 L100 30 L0 30Z" fill="var(--sun-yellow)"/>
    <path d="M0 26 C38 19 68 11 100 5 L100 30 L0 30Z" fill="var(--sun-orange)"/>
    <path d="M0 28 C42 23 72 17 100 12 L100 30 L0 30Z" fill="var(--sun-deep)"/>
  </svg>
  <div class="contact">Palm Grove, FL 33000 · (954) 555-0142<br>info@meadowlarkmobileultrasound.example<br>www.meadowlarkmobileultrasound.example</div>
</section>

<!-- Business card back -->
<section class="piece card card--back" role="img" aria-label="Card back: bright orange and yellow sunburst gradient"></section>

</body>
</html>
```